Vantorix Business
Card and Letter Head
Creative Brief
Professional
Dalton Prewitt
Owner
7153 Hollow Creek Marlowe, Port Adley QX 40917
sales@vantorix.net
vantorix.net
Custom Integrator
ultimate digital experience

```html
<!DOCTYPE html>
<html lang="en">
<head>
<meta charset="utf-8">
<title>Vantorix Business Card</title>
<link href="https://fonts.googleapis.com/css2?family=Questrial&display=swap" rel="stylesheet">
<style>
  :root {
    --canvas: #ffffff;
    --card-dark: #1e1e1f;
    --card-mid: #3a3a3c;
    --card-light: #4a4a4c;
    --gold: #c9c26a;
    --text-light: #f2f2f2;
    --text-soft: #dcdcdc;
    --mark-fill: #d8d8d8;
    --url-text: #2a2a2a;
  }
  * { margin: 0; padding: 0; box-sizing: border-box; }
  html, body {
    width: 1200px; height: 334px; overflow: hidden;
    background: var(--canvas);
    font-family: "Questrial", "Helvetica Neue", Arial, sans-serif;
  }
  .sheet { position: relative; width: 1200px; height: 334px; }
  .card {
    position: absolute; top: 5px; width: 590px; height: 302px;
    background: radial-gradient(ellipse at 40% 35%, var(--card-light) 0%, var(--card-mid) 40%, var(--card-dark) 100%);
    overflow: hidden;
  }
  .card-front { left: 5px; }
  .card-back { left: 629px; width: 566px; }

  .holder { position: absolute; top: 14px; right: 24px; text-align: right; }
  .holder-name { color: var(--gold); font-size: 18px; letter-spacing: 0.5px; }
  .holder-role { color: var(--text-light); font-size: 15px; margin-top: 3px; }

  .front-mark { position: absolute; left: 68px; top: 130px; }
  .front-brand {
    position: absolute; left: 10px; top: 230px;
    color: var(--text-light); font-size: 42px; letter-spacing: 2px;
  }

  .contact {
    position: absolute; left: 312px; top: 200px;
    color: var(--text-soft); font-size: 12px; line-height: 17px; letter-spacing: 0.4px;
    text-transform: uppercase;
  }

  .back-art {
    position: absolute; left: 0; top: 0; width: 100%; height: 100%;
    background: radial-gradient(circle at 45% 45%, rgba(120,120,122,0.35) 0%, rgba(80,80,82,0.15) 45%, rgba(0,0,0,0) 70%);
  }
  .back-mark { position: absolute; left: 230px; top: 88px; }
  .back-brand {
    position: absolute; left: 0; width: 100%; top: 214px; text-align: center;
    color: var(--text-light); font-size: 38px; letter-spacing: 2px;
  }

  .site-url {
    position: absolute; left: 190px; width: 220px; top: 311px; text-align: center;
    color: var(--url-text); font-size: 14px; letter-spacing: 0.8px; text-transform: uppercase;
  }
</style>
</head>
<body>
<div class="sheet">
  <section class="card card-front">
    <div class="holder">
      <p class="holder-name">Dalton Prewitt</p>
      <p class="holder-role">Owner</p>
    </div>
    <svg class="front-mark" width="84" height="84" viewBox="0 0 84 84" aria-hidden="true">
      <circle cx="42" cy="42" r="40" fill="var(--mark-fill)"/>
    </svg>
    <p class="front-brand">VANTORIX</p>
    <div class="contact">
      <p>7153 Hollow Creek Marlowe,</p>
      <p>Port Adley QX 40917</p>
      <p>PH : 555 014 2267</p>
      <p>Fax : 555 018 7731</p>
      <p>Email : sales@vantorix.net</p>
    </div>
  </section>

  <section class="card card-back">
    <div class="back-art" role="img" aria-label="Large faint decorative emblem in soft grey tones"></div>
    <svg class="back-mark" width="104" height="104" viewBox="0 0 104 104" aria-hidden="true">
      <circle cx="52" cy="52" r="50" fill="var(--mark-fill)"/>
    </svg>
    <p class="back-brand">VANTORIX</p>
  </section>

  <p class="site-url">vantorix.net</p>
</div>
</body>
</html>
```